Web design for construction/ handyman company. We are a new company and trying to brand ourselves.

We have a logo with a character already in place and want a user friendly and simple site. I'm attaching our logo designs with our Crocodile character to get an idea of our logo. We want people to remember us and our site. The name we chose was so we could use a logo with a character. Our name is Pelican Builders LLC.

Target Market(s)

New clients

Industry/Entity Type

Contractor

Coding

Coded - Design and coding required

Number of Pages Required

4 page

Font styles to use
Sans Serif

Requirements
Must have
• About Us Page, What we do (not sure what to call this), Contact Us, Home Page. Would like the same colors as on our business card designs to be used on the website.
Nice to have
• We eventually want a project page to add photos of projects but thats not necessary now. Would be nice to use the crocodile theme, hammer or something similar somehow in the page names or clicks.

```html
<!DOCTYPE html>
<html lang="en">
<head>
<meta charset="utf-8">
<title>Pelican Builders LLC</title>
<link href="https://fonts.googleapis.com/css2?family=Open+Sans:ital,wght@0,400;0,600;0,700;0,800;1,400&display=swap" rel="stylesheet">
<style>
:root{
  --green:#3f9a1c;
  --green-dark:#24700f;
  --green-light:#7cc242;
  --blue:#0f4f9a;
  --blue-dark:#0a3672;
  --blue-light:#2f7fd1;
  --ink:#222;
  --muted:#555;
  --paper:#fff;
  --mist:#eef1f6;
}
*{box-sizing:border-box;margin:0;padding:0}
html,body{width:1200px;height:2836px;overflow:hidden}
body{font-family:"Open Sans",Arial,sans-serif;color:var(--ink);background:var(--paper);position:relative}
.abs{position:absolute}

/* header */
.site-header{left:0;top:0;width:1200px;height:110px;background:linear-gradient(180deg,rgba(40,120,20,.95),rgba(30,95,15,.6) 70%,rgba(30,95,15,0));z-index:3}
.brand{left:36px;top:20px;display:flex;align-items:center;gap:12px}
.brand-mark{width:44px;height:44px;border-radius:50%;background:var(--green-light)}
.brand-name{font-weight:800;font-size:30px;color:#fff;line-height:1}
.phone{right:40px;top:18px;display:flex;align-items:center;gap:10px;color:#fff;font-weight:700;font-size:24px}
.main-nav{right:40px;top:64px;display:flex;gap:30px}
.main-nav a{color:#fff;font-size:14px;font-weight:600;text-decoration:none;text-transform:uppercase}
.main-nav a.active{border-bottom:3px solid #fff;padding-bottom:4px}

/* hero */
.hero{left:0;top:0;width:1200px;height:560px;background:linear-gradient(160deg,#dfe6ee 0%,#b9c7d6 45%,#8b9db4 100%)}
.hero-caption{left:0;top:440px;width:1200px;height:100px;background:linear-gradient(90deg,rgba(10,54,114,.9),rgba(47,127,209,.85),rgba(10,54,114,.9));color:#fff;text-align:center;font-size:22px;font-weight:600;padding-top:18px;line-height:32px}

.wave{left:0;width:1200px}

/* section titles */
.section-title{font-size:40px;font-weight:800;color:var(--ink);text-transform:uppercase}
.section-sub{font-size:20px;font-weight:700;color:var(--green)}
.center{text-align:center;width:1200px;left:0}

/* about */
.about{left:0;top:560px;width:1200px;height:660px;background:linear-gradient(180deg,#fff,#f2f4f8)}
.about-text{left:80px;width:600px;font-size:15px;line-height:23px;color:var(--muted)}
.about-text p{margin-bottom:22px}
.about-video{left:730px;top:800px;width:410px;height:190px;background:linear-gradient(135deg,#6d8fb0,#c9b79a 60%,#7f97ad)}
.play{left:905px;top:865px}
.btn-outline{left:80px;top:1050px;width:156px;height:40px;border:2px solid #555;border-radius:6px;font-size:13px;font-weight:700;text-align:center;line-height:36px;color:#333;background:#fff}

/* services */
.services{left:0;top:1300px;width:1200px;height:440px;background:linear-gradient(180deg,#fff,#eef1f6)}
.cards{left:70px;top:1430px;display:flex;gap:18px}
.card{width:252px;height:236px;border-radius:6px;color:#fff;text-align:center;padding-top:16px;position:relative}
.card.green{background:linear-gradient(180deg,var(--green-light),var(--green-dark))}
.card.blue{background:linear-gradient(180deg,var(--blue-light),var(--blue-dark))}
.icon-ring{width:74px;height:74px;border-radius:50%;border:3px solid #fff;margin:0 auto;display:flex;align-items:center;justify-content:center}
.card h3{font-size:16px;font-weight:600;margin-top:10px}
.card p{font-size:11px;line-height:14px;padding:6px 20px 0}
.card .more{position:absolute;left:26px;bottom:16px;width:200px;height:22px;background:#fff;color:#333;border-radius:3px;font-size:10px;font-weight:700;text-align:left;padding-left:12px;line-height:22px}
.card .more span{position:absolute;right:12px}

/* projects */
.projects{left:0;width:1200px;background:#fff}
.project-row{left:110px;top:1880px;display:flex;gap:22px}
.project{width:310px;height:196px;position:relative}
.project:nth-child(1){background:linear-gradient(160deg,#cfd9e4,#8d9fb2 60%,#5c6f82)}
.project:nth-child(2){background:linear-gradient(160deg,#9fb4cb,#d8c9b0 55%,#6e7d66)}
.project:nth-child(3){background:linear-gradient(160deg,#2b3c5e,#a0793e 55%,#3b4a63)}
.project-cap{position:absolute;left:0;bottom:0;width:100%;height:44px;background:rgba(0,0,0,.55);color:#fff;padding:5px 14px;font-size:12px;line-height:16px}
.project-cap b{display:block;color:#f3c24a;font-size:13px}

/* testimonials */
.clients{left:0;width:1200px;background:linear-gradient(180deg,#fff,#eef1f6)}
.quote{left:240px;top:2290px;width:720px;font-size:14px;line-height:21px;color:var(--muted)}
.quote .by{margin-top:6px;font-style:italic}
.arrow{top:2326px;font-size:30px;color:#555;font-weight:700}

/* contact */
.contact{left:0;top:2490px;width:1200px;height:310px;background:linear-gradient(180deg,var(--green-light),var(--green-dark))}
.contact-title{color:#fff;font-size:36px;font-weight:800;text-transform:uppercase}
.contact-info{left:190px;top:2596px;color:#fff;font-size:14px}
.contact-info li{list-style:none;display:flex;align-items:center;gap:16px;height:50px}
.info-icon{width:38px;height:38px;border-radius:50%;background:var(--blue);display:flex;align-items:center;justify-content:center}
.contact-form{left:610px;top:2586px;width:520px;height:190px;border:1px solid rgba(255,255,255,.6);background:rgba(0,0,0,.12);padding:14px}
.field{position:absolute;height:30px;border:1px solid rgba(255,255,255,.7);color:#fff;font-size:12px;padding-left:8px;line-height:28px}
.btn{position:absolute;width:112px;height:34px;background:var(--blue);color:#fff;font-weight:700;font-size:13px;text-align:center;line-height:34px}

.site-footer{left:0;top:2800px;width:1200px;height:36px;background:#f7f7f7;text-align:center;font-size:11px;line-height:36px;color:#555}
</style>
</head>
<body>

<div class="abs hero" role="img" aria-label="Illustration of a house model resting on architectural blueprints"></div>
<header class="abs site-header">
  <div class="abs brand"><span class="brand-mark"></span><span class="brand-name">Pelican Builders</span></div>
  <div class="abs phone">
    <svg width="26" height="26" viewBox="0 0 24 24"><circle cx="12" cy="12" r="11" fill="none" stroke="#fff" stroke-width="2"/><path d="M8 6l2 3-1 2c1 2 2 3 4 4l2-1 3 2-1 2c-5 0-10-5-10-10z" fill="#fff"/></svg>
    1.800.555.0142
  </div>
  <nav class="abs main-nav">
    <a class="active" href="#">Home</a><a href="#">About Us</a><a href="#">Our Services</a><a href="#">Projects</a><a href="#">Contact Us</a>
  </nav>
</header>
<div class="abs hero-caption">Lorem ipsum dolor sit amet, consectetuer adipiscing elit, sed diam nonummy nibh euismod<br>tincidunt ut laoreet dolore magna aliquam erat volutpat.</div>
<svg class="abs wave" style="top:530px" height="60" viewBox="0 0 1200 60" preserveAspectRatio="none"><path d="M0 10 Q600 70 1200 10 L1200 60 L0 60Z" fill="#fff"/><path d="M0 10 Q600 70 1200 10" fill="none" stroke="#0f4f9a" stroke-width="6"/></svg>

<section class="abs about"></section>
<h2 class="abs section-title" style="left:80px;top:612px">About Us</h2>
<p class="abs section-sub" style="left:80px;top:664px">Providing Quality Expert Advise &amp; Friendly Professional Service</p>
<div class="abs about-text" style="top:715px">
  <p>Lorem ipsum dolor sit amet, consectetuer adipiscing elit, sed diam nonummy nibh euismod tincidunt ut laoreet dolore magna aliquam erat volutpat. Ut wisi enim ad minim veniam, quis nostrud exerci tation ullamcorper suscipit lobortis nisl ut aliquip ex ea commodo consequat.</p>
  <p>Duis autem vel eum iriure dolor in hendrerit in vulputate velit esse molestie consequat, vel illum dolore eu feugiat nulla facilisis at vero eros et accumsan et iusto odio dignissim qui blandit praesent luptatum zzril delenit augue duis dolore te feugait nulla facilisi. Nam liber tempor cum soluta nobis eleifend option congue nihil imperdiet doming id quod mazim placerat facer possim assum.</p>
  <p>Typi non habent claritatem insitam est usus legentis in iis qui facit eorum claritatem. Investigationes demonstraverunt lectores legere me lius quod ii legunt saepius.</p>
</div>
<div class="abs about-video" role="img" aria-label="Video still of builders laying bricks on a site"></div>
<svg class="abs play" width="60" height="60" viewBox="0 0 60 60"><circle cx="30" cy="30" r="28" fill="rgba(255,255,255,.85)"/><path d="M24 18 L42 30 L24 42Z" fill="#333"/></svg>
<div class="abs btn-outline">DISCOVER MORE</div>

<svg class="abs wave" style="top:1200px" height="110" viewBox="0 0 1200 110" preserveAspectRatio="none"><path d="M0 20 Q600 100 1200 20 L1200 110 L0 110Z" fill="#fff"/><path d="M0 10 Q600 100 1200 10" fill="none" stroke="#7cc242" stroke-width="10"/><path d="M0 24 Q600 112 1200 24" fill="none" stroke="#0f4f9a" stroke-width="8"/></svg>

<section class="abs services"></section>
<h2 class="abs section-title center" style="top:1320px">Our Services</h2>
<p class="abs section-sub center" style="top:1374px">Leading at Construction And Development</p>
<div class="abs cards">
  <div class="card green"><div class="icon-ring"><svg width="38" height="38" viewBox="0 0 24 24" fill="none" stroke="#fff" stroke-width="2"><rect x="3" y="3" width="14" height="18"/><path d="M8 15 L19 4 L21 6 L10 17 L7 18Z"/></svg></div><h3>Drafting</h3><p>Lorem ipsum dolor sit amet, consectetuer adipiscing elit, sed diam nonummy.</p><div class="more">READ MORE<span>›</span></div></div>
  <div class="card blue"><div class="icon-ring"><svg width="38" height="38" viewBox="0 0 24 24" fill="none" stroke="#fff" stroke-width="2"><path d="M4 21 V4 H18 M4 8 H16 M14 4 V12 M12 14 h4 v4 h-4z"/></svg></div><h3>Construction</h3><p>Lorem ipsum dolor sit amet, consectetuer adipiscing elit, sed diam nonummy.</p><div class="more">READ MORE<span>›</span></div></div>
  <div class="card green"><div class="icon-ring"><svg width="38" height="38" viewBox="0 0 24 24" fill="none" stroke="#fff" stroke-width="2"><rect x="5" y="4" width="14" height="17" rx="1"/><circle cx="12" cy="12" r="3"/><path d="M9 4 V2 H15 V4"/></svg></div><h3>Project Management</h3><p>Lorem ipsum dolor sit amet, consectetuer adipiscing elit, sed diam nonummy.</p><div class="more">READ MORE<span>›</span></div></div>
  <div class="card blue"><div class="icon-ring"><svg width="38" height="38" viewBox="0 0 24 24" fill="none" stroke="#fff" stroke-width="2"><path d="M6 4 H18 L12 10 L18 16 H6 L12 20"/></svg></div><h3>Civil Engineering</h3><p>Lorem ipsum dolor sit amet, consectetuer adipiscing elit, sed diam nonummy.</p><div class="more">READ MORE<span>›</span></div></div>
</div>

<svg class="abs wave" style="top:1690px" height="90" viewBox="0 0 1200 90" preserveAspectRatio="none"><path d="M0 60 Q600 0 1200 60 L1200 90 L0 90Z" fill="#fff"/><path d="M0 56 Q600 -6 1200 56" fill="none" stroke="#0f4f9a" stroke-width="8"/><path d="M0 70 Q600 8 1200 70" fill="none" stroke="#7cc242" stroke-width="6"/></svg>

<section class="abs projects" style="top:1780px;height:350px"></section>
<h2 class="abs section-title center" style="top:1790px">Featured Projects</h2>
<div class="abs project-row">
  <div class="project" role="img" aria-label="Photo of a modern white two-storey home"><div class="project-cap"><b>Residential</b>Lorem ipsum dolor sit amet</div></div>
  <div class="project" role="img" aria-label="Photo of a contemporary villa with a lawn"><div class="project-cap"><b>Beach Villa</b>Lorem ipsum dolor sit amet</div></div>
  <div class="project" role="img" aria-label="Photo of a lit modern house at dusk"><div class="project-cap"><b>Hillside Retreat</b>Lorem ipsum dolor sit amet</div></div>
</div>

<section class="abs clients" style="top:2130px;height:360px"></section>
<svg class="abs wave" style="top:2130px" height="80" viewBox="0 0 1200 80" preserveAspectRatio="none"><path d="M0 10 Q600 80 1200 10" fill="none" stroke="#7cc242" stroke-width="6"/><path d="M0 22 Q600 92 1200 22" fill="none" stroke="#0f4f9a" stroke-width="8"/></svg>
<h2 class="abs section-title center" style="top:2226px">What Our Clients Say</h2>
<div class="abs quote">
  <p>Lorem ipsum dolor sit amet, consectetuer adipiscing elit, sed diam nonummy nibh euismod tincidunt ut laoreet dolore magna aliquam erat volutpat. Ut wisi enim ad minim veniam, quis nostrud exerci tation ullamcorper suscipit lobortis nisl ut aliquip ex ea commodo consequat. Duis autem vel eum iriure dolor in hendrerit in vulputate velit esse molestie consequat, vel illum dolore eu feugiat nulla facilisis at vero eros.</p>
  <p class="by">Many kind regards,<br>– Laura Finch –</p>
</div>
<div class="abs arrow" style="left:160px">‹</div>
<div class="abs arrow" style="left:1020px">›</div>

<svg class="abs wave" style="top:2458px" height="34" viewBox="0 0 1200 34" preserveAspectRatio="none"><path d="M0 34 Q600 -10 1200 34Z" fill="#7cc242"/></svg>
<section class="abs contact"></section>
<h2 class="abs contact-title center" style="top:2506px">Contact Us</h2>
<ul class="abs contact-info">
  <li><span class="info-icon"><svg width="18" height="18" viewBox="0 0 24 24"><path d="M12 2a7 7 0 0 0-7 7c0 5 7 13 7 13s7-8 7-13a7 7 0 0 0-7-7zm0 9a2 2 0 1 1 0-4 2 2 0 0 1 0 4z" fill="#fff"/></svg></span>Corporate Address</li>
  <li><span class="info-icon"><svg width="18" height="18" viewBox="0 0 24 24"><path d="M6 3l3 4-2 2c1 3 4 6 7 7l2-2 4 3-2 3C10 20 4 14 4 5z" fill="#fff"/></svg></span>Corporate Phone</li>
  <li><span class="info-icon"><svg width="18" height="18" viewBox="0 0 24 24"><rect x="3" y="6" width="18" height="12" fill="none" stroke="#fff" stroke-width="2"/><path d="M3 6l9 7 9-7" fill="none" stroke="#fff" stroke-width="2"/></svg></span>info@pelicanbuilders.com</li>
</ul>
<form class="abs contact-form">
  <div class="field" style="left:14px;top:14px;width:240px">Name</div>
  <div class="field" style="left:14px;top:54px;width:240px">Phone Number</div>
  <div class="field" style="left:14px;top:94px;width:240px">Email Address</div>
  <div class="field" style="left:266px;top:14px;width:238px;height:110px">Message / Comment</div>
  <div class="btn" style="left:266px;top:140px">SEND</div>
  <div class="btn" style="left:392px;top:140px">RESET</div>
</form>

<footer class="abs site-footer">© 2013 PELICAN BUILDERS LLC. ALL RIGHTS RESERVED</footer>
</body>
</html>
```